Marwick home cleaning

Design a car wrap for a home cleaning company. The name company Marwick Home cleaning. slogan " we clean, you relax" our instgram is @marwickhc

Target Market(s)

Homes, apts, offices, villas

Industry/Entity Type

Home cleaning

Colors
0054AA
0677BA
7BADD7
CADEEF
E8F1F8
0094D4
00A9DD
6FCCEA
C7EBF8
E9F6FB
FFC000
F8CF3A
FAE287
FDF2CF
FEFAEE

Requirements
Must have
• Home cleaning,
Nice to have
• i want simple design straign not too much wrap, an image clearly tells you about the company along with sname slogan and contact details phone, instgram, website

```html
<!DOCTYPE html>
<html lang="en">
<head>
<meta charset="utf-8">
<title>Marwick Home cleaning – Vehicle Wrap</title>
<link href="https://fonts.googleapis.com/css2?family=Open+Sans:wght@400;600;700&display=swap" rel="stylesheet">
<style>
  :root {
    --backdrop: #141414;
    --panel-white: #ffffff;
    --deep-blue: #0054AA;
    --mid-blue: #0677BA;
    --sky-blue: #0094D4;
    --bright-blue: #00A9DD;
    --soft-blue: #6FCCEA;
    --brand-blue: #1f8fd6;
    --tag-grey: #555a60;
    --slogan-green: #45d62e;
  }
  * { margin: 0; padding: 0; box-sizing: border-box; }
  html, body {
    width: 1200px;
    height: 679px;
    overflow: hidden;
    background: var(--backdrop);
  }
  .wrap-canvas {
    position: relative;
    width: 1200px;
    height: 679px;
    font-family: "Open Sans", Arial, sans-serif;
  }
  .wrap-art {
    position: absolute;
    inset: 0;
  }
  .brand-block {
    position: absolute;
    left: 556px;
    top: 318px;
  }
  .brand-name {
    display: block;
    font-size: 70px;
    font-weight: 600;
    line-height: 1;
    letter-spacing: 1px;
    color: var(--brand-blue);
  }
  .brand-tagline {
    display: block;
    margin: 6px 0 0 16px;
    font-size: 16px;
    font-weight: 400;
    line-height: 1.2;
    color: var(--tag-grey);
  }
  .slogan {
    position: absolute;
    left: 0;
    width: 1200px;
    top: 436px;
    padding-left: 18px;
    text-align: center;
    font-size: 27px;
    font-weight: 700;
    letter-spacing: 4px;
    color: var(--slogan-green);
    text-shadow: 0 2px 3px rgba(0, 0, 0, 0.35);
  }
</style>
</head>
<body>
<main class="wrap-canvas">
  <svg class="wrap-art" width="1200" height="679" viewBox="0 0 1200 679" xmlns="http://www.w3.org/2000/svg">
    <defs>
      <linearGradient id="bubbleTone" x1="0" y1="0" x2="0" y2="1">
        <stop offset="0" stop-color="#1a63c9"/>
        <stop offset="1" stop-color="#0a4fb8"/>
      </linearGradient>
      <linearGradient id="suppliesTone" x1="0" y1="0" x2="1" y2="1">
        <stop offset="0" stop-color="#6FCCEA"/>
        <stop offset="0.55" stop-color="#2fb7a8"/>
        <stop offset="1" stop-color="#8fd46a"/>
      </linearGradient>
      <linearGradient id="frontStripeTone" x1="0" y1="0" x2="1" y2="0">
        <stop offset="0" stop-color="#6FCCEA" stop-opacity="0"/>
        <stop offset="0.35" stop-color="#6FCCEA"/>
        <stop offset="1" stop-color="#00A9DD"/>
      </linearGradient>
    </defs>

    <!-- white body panel -->
    <rect class="panel-body" x="110" y="200" width="1000" height="290" rx="40" fill="var(--panel-white)"/>

    <!-- bubbly blue field: rear section and lower band -->
    <path class="bubble-field" role="img" aria-label="Blue soap bubble texture"
          d="M150 200 H345 C300 260 310 360 380 400 C470 440 600 420 760 415 C900 410 1020 395 1110 385 V450 Q1110 490 1070 490 H150 Q110 490 110 450 V240 Q110 200 150 200 Z"
          fill="url(#bubbleTone)"/>

    <!-- layered swoop bands -->
    <path class="swoop swoop-outer" d="M345 200 H372 C335 265 345 350 405 388 C470 420 560 412 620 410 C520 425 430 425 378 398 C312 362 302 262 345 200 Z" fill="var(--sky-blue)"/>
    <path class="swoop swoop-inner" d="M372 200 H392 C360 262 368 340 425 375 C480 405 560 408 620 410 C560 412 470 420 405 388 C345 350 335 265 372 200 Z" fill="var(--soft-blue)"/>

    <!-- front stripe tapering out of the lower band -->
    <path class="swoop swoop-front" d="M700 417 C850 410 990 392 1110 368 V385 C1020 395 900 410 760 415 Z" fill="url(#frontStripeTone)"/>

    <!-- cleaning supplies artwork area -->
    <rect class="supplies-art" role="img" aria-label="Bucket of cleaning supplies: spray bottles, gloves, squeegee, mop and detergent"
          x="372" y="282" width="164" height="140" rx="18" fill="url(#suppliesTone)"/>
  </svg>

  <div class="brand-block">
    <span class="brand-name">MARWICK</span>
    <span class="brand-tagline">Cleaning Services</span>
  </div>
  <div class="slogan">WE CLEAN - YOU RELAX</div>
</main>
</body>
</html>
```